Willowmere Cremations Business Cards

To create a business card for my company Willowmere Cremations. Remember it is a cremation company.
We want to make sure people have a business card and information. Something modern, professional
100% Online
Prices starting at $695 all-inclusive (prices subject to change without notice).
A business card is the first point of contact with the prospective client.

Contact Information for Business Card

(305) 472-8163
www.WillowmereCremationsMiami.example
willowmerecremations@mailbox.example

Requirements
Must have
• 100% Online
Prices starting at $695 all-inclusive (prices subject to change without notice)

(305) 472-8163

Must match logo style
Should not have
• No black backgrounds. Please only use the white, orange and blue from the logo

```html
<!DOCTYPE html>
<html lang="en">
<head>
<meta charset="utf-8">
<title>Willowmere Cremations – Business Cards</title>
<link rel="stylesheet" href="https://fonts.googleapis.com/css2?family=Montserrat:wght@600;700&family=Open+Sans:wght@400;600;700&display=swap">
<style>
  :root {
    --page: #e6e8eb;
    --card: #ffffff;
    --card-edge: #d5d9de;
    --orange: #f07a2a;
    --orange-light: #f7a13a;
    --blue: #1a9be0;
  }
  * { box-sizing: border-box; margin: 0; padding: 0; }
  html, body { width: 1200px; height: 1200px; overflow: hidden; }
  body {
    background: var(--page);
    font-family: "Open Sans", Arial, sans-serif;
    position: relative;
  }
  .card {
    position: absolute;
    left: 180px;
    width: 840px;
    height: 480px;
    background: var(--card);
    border: 1px solid var(--card-edge);
    border-radius: 26px;
  }
  .card--front { top: 90px; }
  .card--back { top: 630px; }

  /* Brand mark */
  .brand-mark {
    position: absolute;
    display: flex;
    align-items: center;
  }
  .brand-mark__dot {
    width: 150px; height: 150px; border-radius: 50%;
    background: linear-gradient(135deg, var(--orange) 0%, var(--orange-light) 100%);
  }
  .brand-mark__name {
    font-family: "Open Sans", Arial, sans-serif;
    font-weight: 700;
    color: var(--blue);
    text-transform: uppercase;
    letter-spacing: 2px;
    line-height: 1.15;
  }

  /* Front */
  .card--front .brand-mark {
    top: 70px; left: 0; right: 0;
    flex-direction: column;
    gap: 18px;
  }
  .card--front .brand-mark__name { font-size: 26px; }

  .tagline {
    position: absolute;
    left: 70px; right: 70px; top: 300px;
    display: flex; align-items: center; gap: 22px;
  }
  .tagline__rule { flex: 1; height: 2px; background: var(--blue); }
  .tagline__text {
    font-family: "Montserrat", Arial, sans-serif;
    font-weight: 700; font-size: 20px;
    color: var(--blue);
    letter-spacing: 0.5px;
  }
  .pricing {
    position: absolute;
    left: 0; right: 0; top: 345px;
    text-align: center;
    color: var(--orange);
  }
  .pricing__lead { font-weight: 700; font-size: 22px; letter-spacing: 0.3px; }
  .pricing__note { font-weight: 400; font-size: 16px; }

  /* Back */
  .card--back .brand-mark {
    top: 40px; right: 50px;
    flex-direction: column; gap: 10px;
  }
  .card--back .brand-mark__dot { width: 110px; height: 110px; }
  .card--back .brand-mark__name { font-size: 22px; text-align: center; }

  .contact {
    position: absolute;
    left: 70px; bottom: 50px;
  }
  .contact__name {
    font-weight: 700; font-size: 34px;
    color: var(--orange);
    text-transform: uppercase;
    letter-spacing: 0.5px;
    line-height: 1.1;
  }
  .contact__role {
    font-size: 21px; color: var(--blue);
    margin-bottom: 26px;
  }
  .contact__list { list-style: none; }
  .contact__item {
    display: flex; align-items: center; gap: 12px;
    font-size: 20px; color: var(--blue);
    line-height: 1.5;
  }
  .contact__icon { width: 18px; height: 18px; fill: var(--orange); flex: none; }
</style>
</head>
<body>

  <section class="card card--front">
    <div class="brand-mark">
      <div class="brand-mark__dot" aria-hidden="true"></div>
      <div class="brand-mark__name">Willowmere Cremations</div>
    </div>
    <div class="tagline">
      <span class="tagline__rule"></span>
      <span class="tagline__text">100% ONLINE</span>
      <span class="tagline__rule"></span>
    </div>
    <p class="pricing">
      <span class="pricing__lead">Prices starting at $695 all-inclusive</span>
      <span class="pricing__note">(prices subject to change without notice)</span>
    </p>
  </section>

  <section class="card card--back">
    <div class="brand-mark">
      <div class="brand-mark__dot" aria-hidden="true"></div>
      <div class="brand-mark__name">Willowmere<br>Cremations</div>
    </div>
    <div class="contact">
      <h1 class="contact__name">Dana Whitfield</h1>
      <p class="contact__role">Account Executive</p>
      <ul class="contact__list">
        <li class="contact__item">
          <svg class="contact__icon" viewBox="0 0 24 24" aria-hidden="true"><path d="M6.6 10.8a15.1 15.1 0 0 0 6.6 6.6l2.2-2.2a1 1 0 0 1 1-.25 11.4 11.4 0 0 0 3.6.57 1 1 0 0 1 1 1V20a1 1 0 0 1-1 1A17 17 0 0 1 3 4a1 1 0 0 1 1-1h3.5a1 1 0 0 1 1 1c0 1.25.2 2.45.57 3.570a1 1 0 0 1-.25 1z"/></svg>
          (305) 472-8163
        </li>
        <li class="contact__item">
          <svg class="contact__icon" viewBox="0 0 24 24" aria-hidden="true"><path d="M2 5h20v14H2z M4 7v.4l8 5.2 8-5.2V7z" fill-rule="evenodd"/></svg>
          willowmerecremations@mailbox.example
        </li>
        <li class="contact__item">
          <svg class="contact__icon" viewBox="0 0 24 24" aria-hidden="true"><path d="M12 2a10 10 0 1 0 0 20 10 10 0 0 0 0-20zm6.9 6h-2.9a15.6 15.6 0 0 0-1.4-3.6A8 8 0 0 1 18.9 8zM12 4c.8 1.2 1.5 2.5 1.9 4h-3.8c.4-1.5 1.1-2.8 1.9-4zM4.3 14a8 8 0 0 1 0-4h3.4a16 16 0 0 0 0 4zm.8 2h2.9c.3 1.3.8 2.5 1.4 3.6A8 8 0 0 1 5.1 16zM8 8H5.1a8 8 0 0 1 4.3-3.6C8.8 5.5 8.3 6.7 8 8zm4 12c-.8-1.2-1.5-2.5-1.9-4h3.8c-.4 1.5-1.1 2.8-1.9 4zm2.3-6H9.7a14.7 14.7 0 0 1 0-4h4.6a14.7 14.7 0 0 1 0 4zm.3 5.6c.6-1.1 1.1-2.3 1.4-3.6h2.9a8 8 0 0 1-4.3 3.6zm1.7-5.6a16 16 0 0 0 0-4h3.4a8 8 0 0 1 0 4z"/></svg>
          www.WillowmereCremationsMiami.example
        </li>
      </ul>
    </div>
  </section>

</body>
</html>
```